Design for schnapps bottle label "Sol Terrado"

Hi! On a small land lot we are producing our own Italian schnapps "Grappa". For the bottles we would like to modernize our current labes that you find below. The two cats looking at each other should remain, but updated and more modern. I am very much looking forward to your suggestions. Best, Joel

Target Market(s)

Schnapps bottle label

Requirements
Must have
• Cats should resemble the cats that are decorating the house entry (see attached), however, should have a more modern appearance.

Text elements should remain: "Grappa", "Sol Terrado", "Legnoso", "[Vintage Year], "Raccolta No", "Vol %"
Should not have
• Current ornament can be used, replaced or deleted (whatever looks best)

```html
<!DOCTYPE html>
<html lang="en">
<head>
<meta charset="utf-8">
<title>Sol Terrado Grappa – Bottle Label</title>
<link href="https://fonts.googleapis.com/css2?family=Ubuntu:wght@300;400;500;700&family=Playfair+Display:ital@1&display=swap" rel="stylesheet">
<style>
  :root {
    --paper: #ffffff;
    --brown: #55390f;
    --gold: #e0a433;
    --gold-light: #f3d27a;
    --gold-deep: #b98318;
    --wine: #8c1c1c;
    --die-line: #cfcfcf;
  }
  html, body {
    margin: 0;
    padding: 0;
    overflow: hidden;
    background: var(--paper);
  }
  .canvas {
    width: 869px;
    height: 1200px;
    display: block;
  }
  .premium { font-family: "Ubuntu", sans-serif; font-weight: 400; font-size: 30px; letter-spacing: 2px; }
  .product { font-family: "Ubuntu", sans-serif; font-weight: 700; font-size: 122px; paint-order: stroke; stroke-width: 5px; stroke-linejoin: round; }
  .vintage { font-family: "Ubuntu", sans-serif; font-weight: 500; font-size: 56px; }
  .connector { font-family: "Playfair Display", serif; font-style: italic; font-size: 34px; }
  .estate { font-family: "Ubuntu", sans-serif; font-weight: 700; font-size: 64px; }
  .spec { font-family: "Ubuntu", sans-serif; font-weight: 300; font-size: 24px; }
  .brown { fill: var(--brown); }
  .gold-stroke { stroke: var(--gold); }
  .wine { fill: var(--wine); }
  .hatch { stroke: var(--brown); stroke-width: 2; }
  .die-cut { fill: var(--paper); stroke: var(--die-line); stroke-width: 1.5; }
</style>
</head>
<body>
<svg class="canvas" viewBox="0 0 869 1200" xmlns="http://www.w3.org/2000/svg">
  <defs>
    <path id="arc-premium" d="M 300,132 Q 434,58 568,132"/>
    <path id="arc-estate" d="M 200,412 Q 434,570 690,400"/>
    <linearGradient id="foil" x1="0" y1="0" x2="1" y2="1">
      <stop offset="0" stop-color="var(--gold-deep)"/>
      <stop offset="0.5" stop-color="var(--gold-light)"/>
      <stop offset="1" stop-color="var(--gold-deep)"/>
    </linearGradient>

    <g id="label-frame-marks">
      <g class="hatch">
        <line x1="262" y1="142" x2="278" y2="122"/>
        <line x1="270" y1="146" x2="286" y2="126"/>
        <line x1="278" y1="150" x2="294" y2="130"/>
        <line x1="574" y1="130" x2="590" y2="150"/>
        <line x1="582" y1="126" x2="598" y2="146"/>
        <line x1="590" y1="122" x2="606" y2="142"/>
      </g>
    </g>
  </defs>

  <!-- Main label -->
  <g class="label label--classic" transform="translate(0,-40)">
    <use href="#label-frame-marks"/>
    <text class="premium brown"><textPath href="#arc-premium" startOffset="50%" text-anchor="middle">PREMIUM</textPath></text>
    <text class="product brown gold-stroke" x="434" y="262" text-anchor="middle">GRAPPA</text>
    <text class="vintage brown" x="434" y="338" text-anchor="middle">Legnoso 2015</text>
    <circle cx="176" cy="366" r="16" fill="var(--gold)" role="img" aria-label="Gold swirl ornament"/>
    <circle cx="692" cy="366" r="16" fill="var(--gold)" role="img" aria-label="Gold swirl ornament"/>
    <text class="connector brown" x="434" y="396" text-anchor="middle">- di -</text>
    <text class="estate brown"><textPath href="#arc-estate" startOffset="50%" text-anchor="middle">Sol Terrado</textPath></text>
    <rect x="130" y="490" width="290" height="150" rx="40" fill="var(--gold)" role="img" aria-label="Illustration of a cat arching its back, facing right"/>
    <rect x="450" y="490" width="290" height="150" rx="40" fill="var(--gold)" role="img" aria-label="Illustration of a cat arching its back, facing left"/>
    <text class="spec brown" x="140" y="690">RACCOLTA NO.01</text>
    <text class="spec brown" x="730" y="690" text-anchor="end">41.0% VOL.</text>
  </g>

  <!-- Die-cut label variant -->
  <path class="die-cut" d="M 224,1160 V 860 Q 224,800 300,775 L 434,735 L 568,775 Q 644,800 644,860 V 1160 Q 644,1180 624,1180 H 244 Q 224,1180 224,1160 Z"/>
  <g class="label label--foil" transform="translate(173.6,746) scale(0.6)">
    <use href="#label-frame-marks"/>
    <text class="premium brown"><textPath href="#arc-premium" startOffset="50%" text-anchor="middle">PREMIUM</textPath></text>
    <text class="product wine gold-stroke" x="434" y="262" text-anchor="middle">GRAPPA</text>
    <text class="vintage brown" x="434" y="338" text-anchor="middle">Legnoso 2015</text>
    <text class="connector brown" x="434" y="396" text-anchor="middle">- di -</text>
    <text class="estate brown"><textPath href="#arc-estate" startOffset="50%" text-anchor="middle">Sol Terrado</textPath></text>
    <rect x="130" y="490" width="290" height="150" rx="40" fill="url(#foil)" role="img" aria-label="Gold foil illustration of a cat arching its back, facing right"/>
    <rect x="450" y="490" width="290" height="150" rx="40" fill="url(#foil)" role="img" aria-label="Gold foil illustration of a cat arching its back, facing left"/>
    <text class="spec brown" x="140" y="690">RACCOLTA NO.01</text>
    <text class="spec brown" x="730" y="690" text-anchor="end">41.0% VOL.</text>
  </g>
</svg>
</body>
</html>
```